Flyer for the Radiant Harvest Worship Day

I am looking to create a flyer for a one day prayer retreat our church is organizing.
This flyer will be posted on social media, websites and will also be printed so it can be mailed to people.
I am looking for something professional, with good use of our logo and band colors (logo colors).
I am counting on the designer's skill, creativity, art and knowledge of media communication to produce a flyer that will effectively and quickly convey the message we are trying to spread.
CONTENT OF THE FLYER:
Event title: Radiant Harvest Worship Day
Date: Tuesday July 2nd, 2019
Time: 11:00AM - 7:00PM
Belmont Hotel, 4875 Maple Ridge Road, Portland, Maine 04219 (Room: Evergreen)
Event Key words to highlight what the event is about: Prayer, Sharing the Word, Panel discussion, prophecy, Impartation.
Key phrases:
A one day prayer retreat.
Jesus Chris is Lord
Contact info:
www.tuvela.org
Phone: 207 583 2194
Email: contact@brookmeadow.org

```html
<!DOCTYPE html>
<html lang="en">
<head>
<meta charset="UTF-8">
<title>Radiant Harvest Worship Day</title>
<link rel="stylesheet" href="https://fonts.googleapis.com/css2?family=Montserrat:wght@500;600;700&family=Roboto+Condensed:wght@700&display=swap">
<style>
  :root {
    --orange: #f7941d;
    --navy: #0e3557;
    --white: #ffffff;
    --ink: #0b0b0b;
    --tone-deep: #101010;
    --tone-mid: #3c3c3c;
    --tone-light: #7a7a7a;
    --tone-pale: #a9a9a9;
  }
  * { margin: 0; padding: 0; box-sizing: border-box; }
  html, body { width: 838px; height: 1200px; overflow: hidden; background: var(--ink); }
  .flyer {
    position: relative;
    width: 838px;
    height: 1200px;
    overflow: hidden;
    font-family: "Montserrat", Arial, sans-serif;
    color: var(--white);
    background: var(--ink);
  }
  .backdrop {
    position: absolute;
    inset: 0;
    background:
      radial-gradient(ellipse 22% 30% at 24% 48%, rgba(169,169,169,0.55) 0%, transparent 70%),
      radial-gradient(ellipse 16% 26% at 50% 52%, rgba(150,150,150,0.45) 0%, transparent 70%),
      radial-gradient(ellipse 30% 10% at 42% 35%, rgba(122,122,122,0.5) 0%, transparent 75%),
      radial-gradient(ellipse 28% 22% at 82% 80%, rgba(160,160,160,0.5) 0%, transparent 70%),
      radial-gradient(ellipse 30% 25% at 8% 78%, rgba(140,140,140,0.45) 0%, transparent 70%),
      radial-gradient(ellipse 40% 20% at 60% 66%, rgba(90,90,90,0.6) 0%, transparent 75%),
      linear-gradient(180deg, var(--tone-deep) 0%, #1c1c1c 22%, var(--tone-mid) 45%, #4a4a4a 70%, #2a2a2a 88%, #151515 100%);
  }
  .keywords {
    position: absolute;
    top: 72px;
    left: 0;
    width: 100%;
    text-align: center;
    font-size: 20.5px;
    font-weight: 600;
    letter-spacing: 0.2px;
  }
  .keywords .sep { color: var(--orange); margin: 0 8px; }
  .title-frame {
    position: absolute;
    left: 119px;
    top: 157px;
    width: 587px;
    height: 214px;
    border: 1.5px solid var(--orange);
  }
  .title-box {
    position: absolute;
    left: 130px;
    top: 167px;
    width: 565px;
    height: 192px;
    background: var(--orange);
    display: flex;
    align-items: center;
    justify-content: center;
  }
  .title {
    font-family: "Roboto Condensed", "Arial Narrow", sans-serif;
    font-weight: 700;
    font-size: 72px;
    line-height: 1.02;
    text-align: center;
  }
  .subtitle {
    position: absolute;
    top: 380px;
    left: 0;
    width: 100%;
    text-align: center;
    font-family: "Roboto Condensed", "Arial Narrow", sans-serif;
    font-weight: 700;
    font-size: 43px;
    letter-spacing: 1.6px;
  }
  .brand {
    position: absolute;
    left: 312px;
    top: 741px;
    width: 200px;
    height: 200px;
    background: var(--navy);
    display: flex;
    align-items: center;
    justify-content: center;
    font-weight: 700;
    font-size: 34px;
    letter-spacing: 2px;
  }
  .details {
    position: absolute;
    top: 970px;
    font-weight: 700;
    font-size: 19.5px;
    line-height: 1.33;
  }
  .venue { left: 26px; }
  .schedule { right: 40px; text-align: right; }
  .rule {
    position: absolute;
    left: 0;
    top: 1094px;
    width: 100%;
    height: 1.5px;
    background: var(--orange);
  }
  .contact {
    position: absolute;
    top: 1119px;
    left: 0;
    width: 100%;
    text-align: center;
    font-weight: 700;
    font-size: 19.5px;
  }
  .contact .sep { margin: 0 16px; }
  .web-band {
    position: absolute;
    left: 0;
    bottom: 0;
    width: 100%;
    height: 39px;
    background: var(--navy);
    display: flex;
    align-items: center;
    justify-content: center;
    font-weight: 700;
    font-size: 19.5px;
  }
</style>
</head>
<body>
  <main class="flyer">
    <div class="backdrop" role="img" aria-label="Black and white photo of a congregation raising their hands in prayer"></div>

    <p class="keywords">Prayer<span class="sep">|</span>Sharing the Word<span class="sep">|</span>Panel Discussion<span class="sep">|</span>Prophecy<span class="sep">|</span>Impartation</p>

    <div class="title-frame"></div>
    <div class="title-box">
      <h1 class="title">Radiant Harvest<br>Worship Day</h1>
    </div>
    <p class="subtitle">A One Day Prayer Retreat</p>

    <div class="brand">TUVELA</div>

    <div class="details venue">
      Venue:<br>
      Belmont Hotel,<br>
      4875 Maple Ridge Road, Portland,<br>
      Maine 04219 (Room: Evergreen)
    </div>
    <div class="details schedule">
      Date:<br>
      Tuesday July 2nd, 2019<br>
      Time:<br>
      11:00AM - 7:00PM
    </div>

    <div class="rule"></div>
    <p class="contact">Phone: 207 583 2194<span class="sep">|</span>Email: contact@brookmeadow.org</p>

    <footer class="web-band">www.tuvela.org</footer>
  </main>
</body>
</html>
```